Marlowe Business Partners Business Card

I'd Like a Two sided Card. Logo was uploaded as an EPS. If you need an additional type, let me know. Colors in Logo are Pantone 289C and Pantone 348C.

I'm thinking of raising the Print on the front, if that matters. Also would like any Vector Art used in the design included with the uploaded files when awarded. If you need any additional info, please let me know. Uploaded card design was for informational purposes only.

The back of the card should be blue, and I like the design included for the back.
Updates

On the Back of the Card, I will probably want my web address. (www.marlowebusinesspartners.example)

Only Square Card Designs Please

Industry/Entity Type

Business

Requirements
Must have
• Should have enough room for longer email addresses in the future.
Nice to have
• email address above WEb URL.

```html
<!DOCTYPE html>
<html lang="en">
<head>
<meta charset="utf-8">
<title>Marlowe Business Partners – Business Card</title>
<link rel="stylesheet" href="https://fonts.googleapis.com/css2?family=Open+Sans:wght@400;600;700&display=swap">
<style>
  :root {
    --navy: #0f2444;
    --band-text: #9fb2d0;
    --green: #138a43;
    --ink: #1f1f1f;
    --paper: #ffffff;
    --stage: #ece9e4;
    --panel: #f1f1f1;
    --mark-grey: #b5bac3;
  }
  * { margin: 0; padding: 0; box-sizing: border-box; }
  html, body { width: 1200px; height: 1191px; overflow: hidden; }
  body {
    position: relative;
    background: var(--stage);
    font-family: "Open Sans", Arial, sans-serif;
    color: var(--ink);
  }
  .card {
    position: absolute;
    width: 934px;
    height: 534px;
    background: var(--paper);
    box-shadow: 0 2px 6px rgba(0,0,0,0.18);
    overflow: hidden;
  }
  .card--front { left: 233px; top: 36px; }
  .card--back { left: 54px; top: 614px; background: var(--navy); border: 1px solid #0a1a33; }

  .brand { position: absolute; display: flex; align-items: center; gap: 24px; }
  .brand__square { width: 115px; height: 115px; background: var(--navy); flex: none; }
  .brand__name {
    font-weight: 600;
    font-size: 44px;
    color: var(--navy);
    white-space: nowrap;
    letter-spacing: 0.5px;
  }
  .card--front .brand { left: 39px; top: 53px; }
  .card--back .brand { left: 149px; top: 164px; }
  .card--back .brand__square { background: var(--green); }
  .card--back .brand__name { color: var(--paper); }

  .contact { position: absolute; left: 39px; top: 246px; font-size: 23px; line-height: 1; }
  .contact__row { display: flex; align-items: center; gap: 6px; height: 40px; }
  .contact__icon { width: 18px; height: 18px; fill: var(--navy); flex: none; }
  .address { position: absolute; left: 39px; top: 384px; font-size: 23px; line-height: 32px; }

  .person { position: absolute; right: 40px; top: 254px; text-align: right; }
  .person__name { font-weight: 700; font-size: 29px; color: var(--navy); line-height: 36px; }
  .person__title { font-size: 22px; color: var(--green); line-height: 32px; }

  .rule { position: absolute; left: 0; right: 0; top: 463px; height: 3px; background: var(--green); }
  .band { position: absolute; left: 0; right: 0; top: 470px; bottom: 0; background: var(--navy); }
  .band__url {
    position: absolute; left: 39px; top: 16px;
    font-size: 24px; letter-spacing: 3px; color: var(--band-text);
  }
  .emblem-panel {
    position: absolute; left: 705px; top: 333px; width: 182px; height: 178px;
    background: var(--panel);
  }
  .emblem-panel__square {
    position: absolute; left: 24px; top: 22px; width: 134px; height: 134px;
    background: var(--mark-grey);
  }

  .back-url {
    position: absolute; left: 0; right: 0; top: 370px; text-align: center;
    font-size: 26px; letter-spacing: 2.5px; color: var(--paper);
  }
</style>
</head>
<body>

  <section class="card card--front" aria-label="Card front">
    <div class="brand">
      <div class="brand__square"></div>
      <div class="brand__name">Marlowe Business Partners</div>
    </div>

    <div class="contact">
      <div class="contact__row">
        <svg class="contact__icon" viewBox="0 0 24 24" aria-hidden="true"><path d="M6.6 10.8a15.1 15.1 0 0 0 6.6 6.6l2.2-2.2c.3-.3.7-.4 1-.2 1.1.4 2.3.6 3.6.6.6 0 1 .4 1 1V20c0 .6-.4 1-1 1A17 17 0 0 1 3 4c0-.6.4-1 1-1h3.5c.6 0 1 .4 1 1 0 1.3.2 2.5.6 3.6.1.3 0 .7-.2 1z"/></svg>
        <span>555.010.1045</span>
      </div>
      <div class="contact__row">
        <svg class="contact__icon" viewBox="0 0 24 24" aria-hidden="true"><path d="M7 1h10a2 2 0 0 1 2 2v18a2 2 0 0 1-2 2H7a2 2 0 0 1-2-2V3a2 2 0 0 1 2-2zm0 3v12h10V4zm5 14a1.5 1.5 0 1 0 0 3 1.5 1.5 0 0 0 0-3z"/></svg>
        <span>555.010.2099</span>
      </div>
      <div class="contact__row">
        <svg class="contact__icon" viewBox="0 0 24 24" aria-hidden="true"><path d="M2 6a2 2 0 0 1 2-2h16a2 2 0 0 1 2 2v12a2 2 0 0 1-2 2H4a2 2 0 0 1-2-2zm2 .5V8l8 5 8-5V6.5l-8 5z"/></svg>
        <span>dwhitlock@marlowebusinesspartners.example</span>
      </div>
    </div>

    <div class="address">
      <div>1200 Harbor Point Lane</div>
      <div>Linden Ridge Commons, Fairview, VA 20100</div>
    </div>

    <div class="person">
      <div class="person__name">Dana J. Whitlock</div>
      <div class="person__title">President</div>
    </div>

    <div class="rule"></div>
    <div class="band">
      <div class="band__url">www.marlowebusinesspartners.example</div>
    </div>

    <div class="emblem-panel">
      <div class="emblem-panel__square"></div>
    </div>
  </section>

  <section class="card card--back" aria-label="Card back">
    <div class="brand">
      <div class="brand__square"></div>
      <div class="brand__name">Marlowe Business Partners</div>
    </div>
    <div class="back-url">www.marlowebusinesspartners.example</div>
  </section>

</body>
</html>
```